Talvero Networks LLC
Consultant, Health Care Operations
Talvero Networks LLC -
Creative Brief
Use specific fonts
I like Calibri, Tahoma, Lucida (rounded but professional) but am open to other similar fonts
Simple
Dwight Pennock
President, CEO
PO BOX 418263 Coral Springs, FL 33077
dwight@talverohub.com
talverohub.com

```html
<!DOCTYPE html>
<html lang="en">
<head>
<meta charset="utf-8">
<title>Talvero Networks LLC — Stationery</title>
<link href="https://fonts.googleapis.com/css2?family=Carlito:wght@400;700&display=swap" rel="stylesheet">
<style>
  :root {
    --ink: #1b1b1b;
    --band: #231f20;
    --accent: #1fa8e0;
    --paper: #ffffff;
    --stage: #ececec;
    --muted: #555555;
    --rule: #bbbbbb;
  }
  * { margin: 0; padding: 0; box-sizing: border-box; }
  html, body { width: 1200px; height: 808px; overflow: hidden; }
  body {
    background: var(--stage);
    font-family: "Carlito", "Calibri", sans-serif;
    color: var(--ink);
    position: relative;
  }
  .piece {
    position: absolute;
    background: var(--paper);
    overflow: hidden;
    box-shadow: 0 2px 6px rgba(0,0,0,.18);
  }
  .piece svg.header { position: absolute; left: 0; top: 0; width: 100%; display: block; }
  .brand {
    position: absolute;
    display: flex;
    align-items: center;
    gap: 6px;
    font-weight: 700;
    color: var(--ink);
    white-space: nowrap;
    line-height: 1;
  }
  .brand .dot { border-radius: 50%; background: var(--accent); flex: none; }
  .brand.on-dark { color: var(--paper); }

  /* Letterhead */
  .letterhead { left: 83px; top: 83px; width: 450px; height: 642px; }
  .letterhead .brand { left: 50%; top: 118px; transform: translateX(-50%); font-size: 26px; }
  .letterhead .brand .dot { width: 20px; height: 20px; }
  .letterhead .footer {
    position: absolute; left: 0; right: 0; bottom: 14px;
    text-align: center; font-size: 8px; line-height: 1.4; color: var(--muted);
  }

  /* Business cards */
  .card { top: 75px; width: 195px; height: 113px; border-radius: 8px; }
  .card-front { left: 600px; }
  .card-back { left: 808px; background: var(--band); }
  .card-front .brand { left: 50%; top: 48px; transform: translateX(-50%); font-size: 10px; gap: 4px; }
  .card-front .brand .dot { width: 8px; height: 8px; }
  .card-front .person {
    position: absolute; left: 12px; top: 76px; font-size: 6.5px; line-height: 1.4; color: var(--muted);
  }
  .card-front .person strong { color: var(--ink); font-size: 7px; }
  .card-front .divider {
    position: absolute; left: 94px; top: 70px; width: 1px; height: 36px; background: var(--rule);
  }
  .card-front .contact {
    position: absolute; left: 101px; top: 69px; font-size: 6px; line-height: 1.38; color: var(--muted);
  }
  .card-back .brand { left: 50%; top: 50%; transform: translate(-50%, -50%); font-size: 13px; gap: 5px; }
  .card-back .brand .dot { width: 11px; height: 11px; }

  /* Envelope front */
  .envelope-front { left: 550px; top: 213px; width: 625px; height: 232px; }
  .envelope-front .brand { left: 28px; top: 78px; font-size: 20px; }
  .envelope-front .brand .dot { width: 16px; height: 16px; }
  .envelope-front .return-address {
    position: absolute; left: 28px; top: 106px; font-size: 7.5px; color: var(--muted);
  }

  /* Envelope back */
  .envelope-back { left: 550px; top: 475px; width: 625px; height: 250px; }
  .envelope-back svg.flap { position: absolute; left: 0; top: 0; width: 100%; display: block; }
  .envelope-back .brand { left: 50%; top: 44px; transform: translateX(-50%); font-size: 17px; }
  .envelope-back .brand .dot { width: 14px; height: 14px; }
</style>
</head>
<body>

<section class="piece letterhead">
  <svg class="header" viewBox="0 0 450 130" aria-hidden="true">
    <path d="M0 0H450V58Q240 98 0 62Z" fill="var(--band)"/>
    <path d="M0 72Q240 110 450 66" fill="none" stroke="var(--accent)" stroke-width="5"/>
  </svg>
  <div class="brand"><span class="dot"></span>Talvero Networks LLC</div>
  <div class="footer">
    PO BOX 418263 Alder Point, FL 33412 &nbsp;Phone 954.555.0142<br>
    dwight@talverohub.com &nbsp;·&nbsp; talverohub.com
  </div>
</section>

<section class="piece card card-front">
  <svg class="header" viewBox="0 0 195 60" aria-hidden="true">
    <path d="M0 0H195V22Q100 40 0 26Z" fill="var(--band)"/>
    <path d="M0 31Q100 46 195 27" fill="none" stroke="var(--accent)" stroke-width="2.5"/>
  </svg>
  <div class="brand"><span class="dot"></span>Talvero Networks LLC</div>
  <div class="person"><strong>Dwight Pennock</strong><br>President, CEO</div>
  <div class="divider"></div>
  <div class="contact">
    PO BOX 418263<br>Alder Point, FL 33412<br>Phone 954.555.0142<br>dwight@talverohub.com<br>talverohub.com
  </div>
</section>

<section class="piece card card-back">
  <div class="brand on-dark"><span class="dot"></span>Talvero Networks LLC</div>
</section>

<section class="piece envelope-front">
  <svg class="header" viewBox="0 0 625 90" aria-hidden="true">
    <path d="M0 0H625V34Q330 70 0 40Z" fill="var(--band)"/>
    <path d="M0 48Q330 80 625 40" fill="none" stroke="var(--accent)" stroke-width="4"/>
  </svg>
  <div class="brand"><span class="dot"></span>Talvero Networks LLC</div>
  <div class="return-address">PO BOX 418263 Alder Point, FL 33412</div>
</section>

<section class="piece envelope-back">
  <svg class="flap" viewBox="0 0 625 110" aria-hidden="true">
    <path d="M0 0H625V18Q612 60 565 100H60Q12 60 0 18Z" fill="var(--band)"/>
  </svg>
  <div class="brand on-dark"><span class="dot"></span>Talvero Networks LLC</div>
</section>

</body>
</html>
```